Stationery & Envelope Design

Executive Style looking stationery & envelope design.
Business Information:
TLR Keystone Properties
7385 Brindle Hollow Lane, Fairbrook, CA 95661-2049
Phone: 916.555.0142
Fax: 916.555.0187

Industry/Entity Type

Business

```html
<!DOCTYPE html>
<html lang="en">
<head>
<meta charset="utf-8">
<title>TLR Keystone Properties – Envelope Set</title>
<link href="https://fonts.googleapis.com/css2?family=Open+Sans:wght@400;600&display=swap" rel="stylesheet">
<style>
  :root {
    --backdrop: #ececec;
    --paper: #f7f7f7;
    --paper-edge: #dcdcdc;
    --flap-shade: #f1f1f1;
    --ink-dark: #3d4652;
    --ink-accent: #2c5490;
    --ink-grey: #6b6b6b;
    --marker: #9aa3ad;
  }
  * { margin: 0; padding: 0; box-sizing: border-box; }
  html, body {
    width: 1200px;
    height: 795px;
    overflow: hidden;
    background: var(--backdrop);
  }
  .canvas {
    position: relative;
    width: 1200px;
    height: 795px;
  }
  .envelope {
    position: absolute;
    width: 520px;
    height: 226px;
    background: var(--paper);
    border: 1px solid var(--paper-edge);
    box-shadow: 0 6px 18px rgba(0, 0, 0, 0.08);
  }
  .envelope--back { left: 60px; top: 150px; overflow: hidden; }
  .envelope--front { left: 620px; top: 420px; }

  .envelope__flap {
    position: absolute;
    left: 0;
    top: 0;
    width: 100%;
    height: 100px;
    background: var(--flap-shade);
    border-bottom: 1px solid var(--paper-edge);
    border-radius: 0 0 14px 14px;
    display: flex;
    align-items: center;
    justify-content: center;
  }

  .brand {
    display: flex;
    align-items: center;
    gap: 6px;
  }
  .brand__marker {
    width: 8px;
    height: 8px;
    background: var(--marker);
  }
  .brand__name {
    font-family: "Open Sans", sans-serif;
    font-weight: 600;
    font-size: 13px;
    color: var(--ink-dark);
    white-space: nowrap;
  }

  .return-block {
    position: absolute;
    left: 26px;
    top: 26px;
  }
  .return-block .brand { margin-bottom: 14px; }
  .return-address { font-style: normal; }
  .return-address__name {
    font-family: "Open Sans", sans-serif;
    font-weight: 600;
    font-size: 8px;
    color: var(--ink-accent);
    letter-spacing: 0.4px;
    margin-bottom: 3px;
    white-space: nowrap;
  }
  .return-address__street {
    font-family: "Open Sans", sans-serif;
    font-weight: 400;
    font-size: 7.5px;
    color: var(--ink-grey);
    letter-spacing: 0.5px;
    white-space: nowrap;
  }
</style>
</head>
<body>
<main class="canvas">
  <section class="envelope envelope--back" aria-label="Envelope back">
    <div class="envelope__flap">
      <div class="brand">
        <span class="brand__marker"></span>
        <span class="brand__name">TLR Keystone Properties</span>
      </div>
    </div>
  </section>

  <section class="envelope envelope--front" aria-label="Envelope front">
    <div class="return-block">
      <div class="brand">
        <span class="brand__marker"></span>
        <span class="brand__name">TLR Keystone Properties</span>
      </div>
      <address class="return-address">
        <p class="return-address__name">TLR Keystone Properties</p>
        <p class="return-address__street">7385 Brindle Hollow Lane, Fairbrook, CA 95661-2049</p>
      </address>
    </div>
  </section>
</main>
</body>
</html>
```